Emergency Management Consulting Flyer

Company name: Stone Harbor Emergency Management

I am looking for a postcard design for my emergency management consulting business. I'm looking for something that has some colors and is double sided, on side with the information on services provided and the other side with the contact information. For the main side I'm looking for the following:

How prepared are you?

Services Provided:
Healthcare Preparedness
EOC Support
Emergency Planning
Mitigation Planning
Business Continuity
Disaster Response
Training and Exercises
Project Management
And more

Affordable for small and large organizations
Stand-by contracts available

On the back side, I'm looking for Contact Us section.

Overall I'm looking for something a bit more modern and need to have at least one disaster photo. If you have questions please message me.

Target Market(s)

Government, Healthcare Facilities, Businesses

Industry/Entity Type

Consulting

Requirements
Must have
• Disaster Picture, modern looking
• For the main side I'm looking for the following:
• How prepared are you?
• Services Provided:
• Healthcare Preparedness
• EOC Support
• Emergency Planning
• Mitigation Planning
• Business Continuity
• Disaster Response
• Training and Exercises
• Project Management
• And more
• Affordable for small and large organizations
• Stand-by contracts available

```html
<!DOCTYPE html>
<html lang="en">
<head>
<meta charset="utf-8">
<title>Stone Harbor Emergency Management – Postcard Front</title>
<link rel="stylesheet" href="https://fonts.googleapis.com/css2?family=Open+Sans:wght@300;400&family=PT+Sans:wght@400;700&display=swap">
<style>
  :root {
    --board: #cccccc;
    --ink: #111111;
    --white: #ffffff;
    --storm-dark: #2c322f;
    --storm-mid: #5f6a64;
    --storm-light: #9aa29c;
    --earth-light: #c9a96a;
    --earth-amber: #e39a2c;
    --earth-rust: #c4461f;
    --band-blue: #1e9ad6;
    --band-orange: #f3a01f;
    --band-grey: #b9b9b9;
  }
  * { margin: 0; padding: 0; box-sizing: border-box; }
  html, body { width: 1200px; height: 1000px; overflow: hidden; }
  body {
    position: relative;
    background: var(--board);
    font-family: "PT Sans", sans-serif;
  }
  .board-title {
    position: absolute;
    top: 72px; left: 0; width: 1200px;
    text-align: center;
    font-family: "Open Sans", sans-serif;
    font-weight: 400;
    font-size: 50px;
    color: var(--ink);
  }
  .postcard {
    position: absolute;
    left: 137px; top: 185px;
    width: 947px; height: 728px;
    overflow: hidden;
  }
  .postcard-art { position: absolute; inset: 0; }
  .brand {
    position: absolute;
    left: 58px; top: 62px;
    display: flex; align-items: center; gap: 10px;
    width: 200px;
  }
  .brand-dot {
    flex: none;
    width: 18px; height: 18px;
    border-radius: 50%;
    background: var(--band-blue);
  }
  .brand-name {
    font-family: "PT Sans", sans-serif;
    font-weight: 700;
    font-size: 17px;
    line-height: 1.15;
    color: var(--white);
  }
  .headline {
    position: absolute;
    left: 0; top: 0;
    font-family: "Open Sans", sans-serif;
    font-weight: 300;
    color: var(--white);
    text-shadow: 0 2px 6px rgba(0,0,0,.35);
  }
  .headline span { position: absolute; white-space: nowrap; line-height: 1; }
  .headline-how { left: 206px; top: 72px; font-size: 100px; }
  .headline-prepared { left: 283px; top: 150px; font-size: 64px; transform: scaleX(.95); transform-origin: left; }
  .headline-question { left: 373px; top: 213px; font-size: 54px; transform: scaleX(.95); transform-origin: left; }
  .services {
    position: absolute;
    left: 645px; top: 398px;
    color: var(--white);
  }
  .services-title {
    font-weight: 700;
    font-size: 21px;
    letter-spacing: .2px;
    margin-bottom: 4px;
  }
  .services-list { list-style: none; padding-left: 4px; }
  .services-list li {
    display: flex; align-items: center; gap: 6px;
    font-size: 22px;
    line-height: 30.6px;
  }
  .tick { width: 13px; height: 13px; flex: none; }
  .services-more { padding-left: 12px; font-size: 22px; line-height: 30.6px; }
</style>
</head>
<body>
  <h1 class="board-title">Post Card - Front</h1>

  <section class="postcard">
    <svg class="postcard-art" width="947" height="728" viewBox="0 0 947 728" xmlns="http://www.w3.org/2000/svg">
      <defs>
        <radialGradient id="storm-sky" cx="0.55" cy="0.3" r="0.8">
          <stop offset="0" stop-color="var(--storm-light)"/>
          <stop offset="0.5" stop-color="var(--storm-mid)"/>
          <stop offset="1" stop-color="var(--storm-dark)"/>
        </radialGradient>
        <linearGradient id="dry-earth" x1="0" y1="0" x2="1" y2="0.4">
          <stop offset="0" stop-color="var(--earth-light)"/>
          <stop offset="0.55" stop-color="var(--earth-amber)"/>
          <stop offset="1" stop-color="var(--earth-rust)"/>
        </linearGradient>
      </defs>
      <rect class="scene-storm" width="947" height="728" fill="url(#storm-sky)"
            role="img" aria-label="Photo of a tornado tearing apart a house in a grassy field"/>
      <path class="scene-earth" d="M0,618 C320,540 660,330 947,85 L947,728 L0,728 Z" fill="url(#dry-earth)"
            role="img" aria-label="Photo of dry, cracked earth tinted orange"/>
      <path class="band-grey" d="M0,528 C260,470 600,290 947,-10 L947,50 C620,320 280,520 0,575 Z" fill="var(--band-grey)" opacity=".45"/>
      <path class="band-orange" d="M0,602 C250,545 480,420 690,292 C480,405 240,505 0,566 Z" fill="var(--band-orange)"/>
      <path class="band-blue" d="M0,618 C320,540 660,330 947,85 L947,28 C660,290 320,520 0,602 Z" fill="var(--band-blue)"/>
    </svg>

    <div class="brand">
      <span class="brand-dot"></span>
      <span class="brand-name">Stone Harbor Emergency Management</span>
    </div>

    <h2 class="headline">
      <span class="headline-how">HOW</span>
      <span class="headline-prepared">PREPARED</span>
      <span class="headline-question">ARE YOU?</span>
    </h2>

    <div class="services">
      <h3 class="services-title">SERVICES PROVIDED:</h3>
      <ul class="services-list">
        <li><svg class="tick" viewBox="0 0 12 12"><path d="M1.5,6.5 L4.5,9.5 L10.5,2.5" fill="none" stroke="#fff" stroke-width="2.2"/></svg>Healthcare Preparedness</li>
        <li><svg class="tick" viewBox="0 0 12 12"><path d="M1.5,6.5 L4.5,9.5 L10.5,2.5" fill="none" stroke="#fff" stroke-width="2.2"/></svg>EOC Support</li>
        <li><svg class="tick" viewBox="0 0 12 12"><path d="M1.5,6.5 L4.5,9.5 L10.5,2.5" fill="none" stroke="#fff" stroke-width="2.2"/></svg>Emergency Planning</li>
        <li><svg class="tick" viewBox="0 0 12 12"><path d="M1.5,6.5 L4.5,9.5 L10.5,2.5" fill="none" stroke="#fff" stroke-width="2.2"/></svg>Mitigation Planning</li>
        <li><svg class="tick" viewBox="0 0 12 12"><path d="M1.5,6.5 L4.5,9.5 L10.5,2.5" fill="none" stroke="#fff" stroke-width="2.2"/></svg>Business Continuity</li>
        <li><svg class="tick" viewBox="0 0 12 12"><path d="M1.5,6.5 L4.5,9.5 L10.5,2.5" fill="none" stroke="#fff" stroke-width="2.2"/></svg>Disaster Response</li>
        <li><svg class="tick" viewBox="0 0 12 12"><path d="M1.5,6.5 L4.5,9.5 L10.5,2.5" fill="none" stroke="#fff" stroke-width="2.2"/></svg>Training and Exercises</li>
        <li><svg class="tick" viewBox="0 0 12 12"><path d="M1.5,6.5 L4.5,9.5 L10.5,2.5" fill="none" stroke="#fff" stroke-width="2.2"/></svg>Project Management</li>
      </ul>
      <p class="services-more">...... And more</p>
    </div>
  </section>
</body>
</html>
```